Book for a presidential campaign

We need a book front cover design for a presidential campaign. The title of the book is "Plant a Thousand Orchards!" Subtitle is "Notes From a Quiet Riverbank" The candidate's name should be on the cover as well, so let's call him "Dale Whitcombe" so you have a name to use in your design. The candidate is nonpartisan, appealing to both liberals and conservatives. The solutions are out of the box and powerful, leading to the benefit of all.

```html
<!DOCTYPE html>
<html lang="en">
<head>
<meta charset="utf-8">
<title>Plant a Thousand Orchards! — Book Cover</title>
<link href="https://fonts.googleapis.com/css2?family=Marcellus&family=Arimo:wght@400&display=swap" rel="stylesheet">
<style>
  :root {
    --gold-deep: #d9a825;
    --gold-light: #f8eca6;
    --ink: #231f20;
    --cream: #f7eeb8;
    --chart-gold: #ddae28;
  }
  * { margin: 0; padding: 0; box-sizing: border-box; }
  html, body {
    width: 848px;
    height: 1200px;
    overflow: hidden;
    background: var(--ink);
  }
  .cover {
    position: relative;
    width: 848px;
    height: 1200px;
    background: var(--ink);
  }
  .title-band {
    height: 460px;
    background: linear-gradient(to bottom, var(--gold-deep) 0%, #e2b73f 40%, var(--gold-light) 100%);
    display: flex;
    flex-direction: column;
    align-items: center;
    justify-content: center;
    padding-top: 10px;
  }
  .title {
    font-family: "Marcellus", serif;
    color: var(--ink);
    text-align: center;
    line-height: 1;
    text-transform: uppercase;
  }
  .title-main {
    display: block;
    font-size: 100px;
    letter-spacing: 2px;
  }
  .title-small {
    display: block;
    font-size: 36px;
    margin: 14px 0 12px;
    letter-spacing: 2px;
  }
  .subtitle {
    font-family: "Arimo", sans-serif;
    color: var(--cream);
    font-size: 29px;
    text-transform: uppercase;
    text-align: center;
    letter-spacing: 0.5px;
    margin-top: 26px;
  }
  .chart {
    display: block;
    margin: 52px auto 0;
  }
  .author {
    display: flex;
    align-items: center;
    justify-content: center;
    gap: 18px;
    margin-top: 46px;
  }
  .author-rule {
    width: 190px;
    height: 2px;
    background: var(--chart-gold);
  }
  .author-name {
    font-family: "Arimo", sans-serif;
    color: var(--cream);
    font-size: 31px;
    text-transform: uppercase;
    letter-spacing: 0.5px;
  }
  .base-rule {
    position: absolute;
    left: 0;
    right: 0;
    top: 1110px;
    height: 2px;
    background: var(--chart-gold);
  }
</style>
</head>
<body>
  <main class="cover">
    <header class="title-band">
      <h1 class="title">
        <span class="title-main">Plant</span>
        <span class="title-small">a Thousand</span>
        <span class="title-main">Orchards!</span>
      </h1>
    </header>
    <p class="subtitle">Notes From a Quiet Riverbank</p>
    <svg class="chart" width="440" height="390" viewBox="0 0 440 390" aria-hidden="true">
      <polyline points="7,0 7,383 440,383" fill="none" stroke="var(--chart-gold)" stroke-width="14"/>
      <rect x="40" y="60" width="74" height="300" fill="var(--chart-gold)"/>
      <rect x="144" y="120" width="74" height="240" fill="var(--chart-gold)"/>
      <rect x="248" y="180" width="74" height="180" fill="var(--chart-gold)"/>
      <rect x="352" y="250" width="74" height="110" fill="var(--chart-gold)"/>
    </svg>
    <div class="author">
      <span class="author-rule"></span>
      <span class="author-name">Dale Whitcombe</span>
      <span class="author-rule"></span>
    </div>
    <div class="base-rule"></div>
  </main>
</body>
</html>
```